Bar and Grill looking or a Responsive Web design

New Bar and Grill in the Toronto area just opened up and is looking for a new wordpress website to start off his business.

Their business revolves around a homey family, upbeat atmosphere. His cuisine is gourmet pub style food. Speciality are home made burgers. 90 Seat restaurant in a very diverse and high density neighbourhood.

Looking for a responsive web design that will focus on a key feature pages.

Homepage
- Navigation is easy and simple, emphasize easy navigation in Mobile view.
- Contact information is a click or touch away

About Page

Menu Page
-Menu styling to be responsive. Very simple navigation through different menus and then menu would appear.

Gallery

Contact page
- Map (not googlesk)
- Contact Details
- Contact/Feedback form

They do have a logo and will be uploaded.

We are open to any designs, as well as designs based off templates that have already been created.

Target Market(s)

Target audience is the varied. They are in an area that's densely populated and very diverse. Looking for a crowd that appreciates a setting for sports, good gourmet pub styled food and a home styled restaurant.

Industry/Entity Type

Restaurant

Colors

Designer to choose colors to be used in the design.

Requirements
Must have
• Menus have to have responsive design for both mobile and tablet/desktop.
Nice to have
• Easy access contact button on mobile view. That way it will act like a webapp so that mobile devices can take advantage of quick touches to get in contact.

```html
<!DOCTYPE html>
<html lang="en">
<head>
<meta charset="utf-8">
<title>Maplewood Bar and Grill</title>
<link href="https://fonts.googleapis.com/css2?family=Roboto+Condensed:wght@400;700&family=Josefin+Sans:ital,wght@0,400;0,600;0,700;1,400&display=swap" rel="stylesheet">
<style>
:root{
  --paper:#ececec;
  --paper-light:#f4f4f4;
  --ink:#2b2623;
  --text:#3a3532;
  --maroon:#7c1519;
  --accent-soft:#c0393b;
  --rule:#b9b9b9;
  --card-border:#cfcfcf;
  --footer:#5e5e5e;
  --footer-dark:#4a4a4a;
  --footer-text:#f1f1f1;
  --head:"Roboto Condensed", sans-serif;
  --body:"Josefin Sans", sans-serif;
}
*{box-sizing:border-box;margin:0;padding:0}
html,body{width:860px;height:1200px;overflow:hidden}
body{position:relative;background:var(--paper);font-family:var(--body);color:var(--text)}
.abs{position:absolute}

/* header */
.site-header{left:0;top:0;width:860px;height:114px;background:var(--paper-light)}
.brand{left:0;width:860px;top:26px;text-align:center;font-family:var(--head);font-weight:700;font-size:38px;letter-spacing:1px;color:var(--ink)}
.brand-mark{display:inline-block;width:10px;height:10px;background:var(--ink);margin-right:10px;vertical-align:middle}
.contact-top{left:645px;top:26px;font-size:10px;line-height:22px;color:var(--ink)}
.contact-top svg{vertical-align:-2px;margin-right:5px}
.main-nav{left:0;top:92px;width:860px;height:16px}
.main-nav::before,.main-nav::after{content:"";position:absolute;top:8px;height:2px;background:var(--rule)}
.main-nav::before{left:0;width:272px}
.main-nav::after{left:584px;width:276px}
.main-nav ul{list-style:none;display:flex;justify-content:center;gap:15px;font-family:var(--head);font-size:13px;letter-spacing:.3px;color:var(--ink)}

/* hero */
.hero{left:0;top:114px;width:860px;height:254px;background:linear-gradient(180deg,#6f8a3c 0%,#8aa24c 35%,#7a5a3a 62%,#5b3b25 100%)}
.hero-photo{left:0;top:0;width:860px;height:254px;background:radial-gradient(ellipse 160px 115px at 480px 130px,#c9853c 0%,#a4612c 55%,rgba(120,75,40,0) 100%)}
.hero-title{left:118px;top:14px;font-family:var(--body);font-weight:400;font-size:22px;line-height:28px;letter-spacing:.5px;color:#fff}
.hero-arrow{top:104px;width:38px;height:38px;border-radius:50%;background:rgba(80,80,60,.45)}
.hero-dots{left:402px;top:236px;display:flex;gap:4px}
.hero-dots span{width:11px;height:11px;background:#fff}
.hero-dots span.active{background:var(--maroon)}

/* welcome */
.welcome-title{left:0;width:860px;top:378px;text-align:center;font-family:var(--head);font-weight:400;font-size:25px;letter-spacing:.5px;color:var(--ink)}
.welcome-text{left:155px;width:550px;top:417px;text-align:center;font-size:8.8px;line-height:17px}
.btn{display:block;background:var(--maroon);color:#fff;font-size:8.5px;text-align:center;line-height:16px}
.welcome-btn{left:387px;top:486px;width:86px}
.divider{left:0;top:544px;width:860px;height:2px;background:var(--rule)}
.utensils{left:405px;top:520px}

/* info cards */
.card{top:575px;width:154px;height:211px;background:var(--paper-light);border:1px solid var(--card-border);border-radius:3px;box-shadow:0 1px 2px rgba(0,0,0,.12)}
.card h3{margin-top:12px;text-align:center;font-family:var(--head);font-weight:400;font-size:12px;letter-spacing:.3px;color:var(--ink)}
.menu-photo{margin:5px 6px 0;height:81px;background:linear-gradient(135deg,#8a5a3c,#b67a4c 50%,#6b3a2a)}
.card p.small{margin:8px 10px 0;text-align:center;font-size:8.5px;line-height:11.5px}
.card .btn{position:absolute;left:33px;width:86px;bottom:12px}
.hours{margin-top:9px;text-align:center;font-size:10px;line-height:13.5px;color:var(--maroon);font-weight:600}
.hours dt{margin-top:7px}
.hours dd{font-weight:600}
.reserve{margin:10px 10px 0;height:124px;background:#d9d9d9;border:1px solid #c4c4c4;border-radius:3px;padding-top:9px}
.reserve h4{text-align:center;font-size:8px;font-weight:700;color:var(--maroon);letter-spacing:.3px}
.field{display:flex;align-items:center;margin:6px 0 0 9px}
.field svg{margin-right:6px}
.select{width:92px;height:15px;background:#fff;border:1px solid #bcbcbc;font-size:8px;line-height:14px;padding-left:8px;position:relative;color:var(--ink)}
.select::after{content:"";position:absolute;right:0;top:0;width:13px;height:13px;border-left:1px solid #bcbcbc;background:#fff}
.select i{position:absolute;right:3px;top:4px;border:4px solid transparent;border-top:5px solid #555;z-index:1}
.reserve .btn{position:static;width:92px;margin:7px 0 0 24px}
.contact-card .name{margin:12px 0 0 11px;font-family:var(--head);font-size:14px;color:var(--ink)}
.contact-row{display:flex;margin:6px 10px 0 11px;font-size:8.5px;line-height:11.5px}
.contact-row svg{flex:none;margin-right:5px;margin-top:1px}

/* testimonial */
.say-title{left:115px;top:822px;font-family:var(--head);font-weight:400;font-size:24px;letter-spacing:.5px;color:var(--ink)}
.quote-mark{left:190px;top:898px;font-family:Georgia, serif;font-size:46px;color:#c8c8c8;line-height:1}
.quote{left:222px;top:914px;width:232px;font-style:italic;font-size:11.5px;line-height:14.8px;color:var(--text)}
.pointer{left:482px;top:930px;width:52px;height:12px;border-radius:6px;background:var(--accent-soft)}
.avatar{left:571px;top:892px;width:86px;height:86px;border-radius:50%;background:#e6e6e6;border:4px solid #f6f6f6;box-shadow:0 0 3px rgba(0,0,0,.25)}
.avatar-fill{left:584px;top:905px;width:60px;height:60px;border-radius:50%;background:#8b8b8b}
.person{left:530px;width:168px;top:985px;text-align:center;font-size:10.5px;line-height:14px;color:var(--ink)}
.person strong{font-weight:400;letter-spacing:.4px}

/* footer */
.site-footer{left:0;top:1031px;width:860px;height:147px;background:var(--footer);color:var(--footer-text)}
.site-footer h4{font-family:var(--head);font-weight:400;font-size:16px}
.foot-links{left:115px;top:6px}
.foot-links ul{list-style:none;font-family:var(--head);font-weight:400;font-size:11.5px;line-height:21px;margin-top:1px}
.foot-social{left:307px;top:6px}
.social-grid{display:grid;grid-template-columns:repeat(2,22px);gap:8px;margin:6px 0 0 15px}
.social-grid span{width:22px;height:22px;border-radius:50%;border:2px solid #9aa3ad;background:#6b6e72}
.foot-map{left:508px;top:6px}
.map{margin-top:5px;width:237px;height:111px;background:linear-gradient(135deg,#e8e6df,#dcd8cc 60%,#cfd9c6)}
.copyright{left:0;top:1178px;width:860px;height:22px;background:var(--footer-dark);color:#c9c9c9;text-align:center;font-size:7.5px;line-height:22px}
</style>
</head>
<body>

<header class="site-header abs">
  <div class="brand abs"><span class="brand-mark"></span>MAPLEWOOD</div>
  <div class="contact-top abs">
    <div><svg width="9" height="8" viewBox="0 0 9 8"><path d="M1 2 Q4.5 -1 8 2 L7 3.5 L5.5 2.5 L3.5 2.5 L2 3.5 Z M2 4 H7 V7.5 H2 Z" fill="#777"/></svg>(416) 555 0142</div>
    <div><svg width="9" height="8" viewBox="0 0 9 8"><path d="M0.5 3 L4.5 0.5 L8.5 3 V7.5 H0.5 Z M0.5 3 L4.5 5.5 L8.5 3" fill="none" stroke="#777"/></svg>info@maplewoodgrill.ca</div>
  </div>
  <nav class="main-nav abs">
    <ul><li>HOME</li><li>ABOUT US</li><li>MENU</li><li>GALLERY</li><li>CONTACT US</li></ul>
  </nav>
</header>

<section class="hero abs">
  <div class="hero-photo abs" role="img" aria-label="Photo of a double cheeseburger on a wooden table with a green garden behind"></div>
  <h1 class="hero-title abs">LOREM IPSUM. PROIN GRAVIDA<br>NIBH VEL VELIT AUCTOR</h1>
  <div class="hero-arrow abs" style="left:104px"><svg width="38" height="38"><path d="M22 11 L14 19 L22 27" fill="none" stroke="#ddd" stroke-width="1.5"/></svg></div>
  <div class="hero-arrow abs" style="left:718px"><svg width="38" height="38"><path d="M16 11 L24 19 L16 27" fill="none" stroke="#ddd" stroke-width="1.5"/></svg></div>
  <div class="hero-dots abs"><span class="active"></span><span></span><span></span><span></span></div>
</section>

<h2 class="welcome-title abs">WELCOME TO MAPLEWOOD BAR AND GRILL</h2>
<p class="welcome-text abs">Lorem Ipsum. Proin gravida nibh vel velit auctor aliquet. Aenean sollicitudin, lorem quis bibendum auctor, nisi elit consequat ipsum, nec sagittis sem nibh id elit. Duis sed odio sit amet nibh vulputate cursus a sit amet mauris. Morbi accumsan ipsum velit. Nam nec tellus a odio tincidunt auctor a ornare odio. Sed non mauris vitae erat consequat auctor eu in elit. Classaptent taciti sociosqu ad litora torquent per conubia nostra, per inceptos himenaeos.</p>
<span class="btn welcome-btn abs">Learn More</span>

<div class="divider abs"></div>
<svg class="utensils abs" width="50" height="46" viewBox="0 0 50 46">
  <rect x="0" y="0" width="50" height="46" fill="var(--paper)"/>
  <ellipse cx="11" cy="8" rx="5" ry="6.5" fill="#888" transform="rotate(-45 11 8)"/>
  <line x1="14" y1="11" x2="42" y2="42" stroke="#888" stroke-width="2.5" stroke-linecap="round"/>
  <path d="M34 3 L40 9 M37 1 L43 7 M40 0 L46 6" stroke="#888" stroke-width="1.6" fill="none"/>
  <line x1="38" y1="8" x2="8" y2="42" stroke="#888" stroke-width="2.5" stroke-linecap="round"/>
</svg>

<article class="card abs" style="left:114px">
  <h3>MENU</h3>
  <div class="menu-photo" role="img" aria-label="Photo of grilled burgers and peppers on a platter"></div>
  <p class="small">Lorem Ipsum. Proin gravida nibh vel velit auctor aliquet. Aenean sollicitudin, lorem quis bibendum auctor, nisi</p>
  <span class="btn">View Our Menu</span>
</article>

<article class="card abs" style="left:273px">
  <h3>OPENING HOURS</h3>
  <dl class="hours">
    <dt>MONDAY</dt><dd>4:00 PM – 12:00 AM</dd>
    <dt>TUESDAY – THURSDAY</dt><dd>12:00 PM – 12:00 AM</dd>
    <dt>FRIDAY – SATURDAY</dt><dd>12:00 PM – 2:00 AM</dd>
    <dt>SUNDAY</dt><dd>12:00 PM – 11:00 PM</dd>
  </dl>
</article>

<article class="card abs" style="left:432px">
  <h3>RESERVATION</h3>
  <div class="reserve">
    <h4>MAKE A RESERVATION</h4>
    <div class="field"><svg width="10" height="9"><rect x="0.5" y="1.5" width="9" height="7" fill="none" stroke="#999"/><line x1="0.5" y1="3.5" x2="9.5" y2="3.5" stroke="#999"/></svg><div class="select">10 - 12 - 2013<i></i></div></div>
    <div class="field"><svg width="10" height="10"><circle cx="5" cy="5" r="4.3" fill="none" stroke="#999"/><path d="M5 2.5 V5 H7" stroke="#999" fill="none"/></svg><div class="select">09 : 00 PM<i></i></div></div>
    <div class="field"><svg width="12" height="9"><circle cx="4" cy="3" r="2" fill="#999"/><circle cx="8.5" cy="3" r="2" fill="#999"/><path d="M0.5 9 Q4 4 7.5 9 Z M5 9 Q8.5 4 12 9 Z" fill="#999"/></svg><div class="select" style="width:90px">2 PEOPLE<i></i></div></div>
    <span class="btn">Find A Table</span>
  </div>
</article>

<article class="card contact-card abs" style="left:591px">
  <h3>CONTACT</h3>
  <div class="name">Maplewood Bar and Grill</div>
  <div class="contact-row"><svg width="8" height="11"><path d="M4 10.5 C1 6 0.5 5 0.5 4 A3.5 3.5 0 0 1 7.5 4 C7.5 5 7 6 4 10.5 Z" fill="none" stroke="#888"/><circle cx="4" cy="4" r="1.2" fill="#888"/></svg><span>Lorem Ipsum. Proin gravida nibh vel velit auctor aliquet Aenean sollicitudin, lorem</span></div>
  <div class="contact-row" style="margin-top:9px"><svg width="9" height="8"><path d="M1 2 Q4.5 -1 8 2 L7 3.5 L5.5 2.5 L3.5 2.5 L2 3.5 Z M2 4 H7 V7.5 H2 Z" fill="#777"/></svg><span>(416) 555 0142</span></div>
  <div class="contact-row" style="margin-top:18px"><svg width="9" height="8"><path d="M0.5 3 L4.5 0.5 L8.5 3 V7.5 H0.5 Z M0.5 3 L4.5 5.5 L8.5 3" fill="none" stroke="#777"/></svg><span>info@maplewoodgrill.ca</span></div>
  <span class="btn">View Details</span>
</article>

<h2 class="say-title abs">WHAT HAPPY CUSTOMER SAY ABOUT MAPLEWOOD</h2>
<div class="quote-mark abs">“</div>
<blockquote class="quote abs">Lorem Ipsum. Proin gravida nibh vel velit auctor aliquet. Aenean sollicitudin, lorem quis bibendum auctor, nisi elit consequat ipsum, nec sagittis sem nibh id elit.</blockquote>
<div class="pointer abs" role="img" aria-label="Decorative red ribbon pointing to the quote"></div>
<div class="avatar abs"></div>
<div class="avatar-fill abs" role="img" aria-label="Customer portrait placeholder"></div>
<div class="person abs"><strong>MAREK OLSEN</strong><br>Toronto</div>

<footer class="site-footer abs">
  <div class="foot-links abs">
    <h4>Brows site</h4>
    <ul><li>Home</li><li>About Us</li><li>Menu</li><li>Gallery</li><li>Contact Us</li></ul>
  </div>
  <div class="foot-social abs">
    <h4>Lets get social</h4>
    <div class="social-grid" aria-label="Social links"><span></span><span></span><span></span><span></span></div>
  </div>
  <div class="foot-map abs">
    <h4>Location map</h4>
    <div class="map" role="img" aria-label="Street map of downtown Toronto with the restaurant location marked"></div>
  </div>
</footer>
<div class="copyright abs">© Copyright 2013 Maplewood Bar and Grill</div>

</body>
</html>
```